Rustic Interior Decoration Artist - Website and Logo Design

I'm a craftsman in the art of rustic interior decoration. My passion goes beyond just creating spaces that recreate comfortable and cozy environments. I invest a lot of energy and creativity on every project, and I want my online presence to reflect that highlighting all the possible details in a way that echoes the art behind what I do for a living. In terms of more information, I would like to highlight the following things through the style of the website: material TONALITY, FORM and mainly TEXTURE.

I have a unique catalogue of the type of decoration that I do (attached are the catalogue photos from two products that can be used: Marlow and Cobalto. I want to be able to showcase to potential clients the product catalogue that I have in person, which is the primary goal of the website. This showcase will be free and with no commitment.

The website will consist basically of 3 different sections: Bio, Projects (with a dedicated page for every project. Use three projects from the ones that I'm attaching) and Contact highlighting that they can request a demo with no commitment. IT SHOULD BE PROVIDED WITH ALL VIEWPORTS.

I do have a Youtube Channel (https://www.vidtubo.example/c/TeodoMarvelrinconesagrestes) and Friendnook (https://www.friendnook.example/teodomarvel/), so that also needs to be highlighted somehow.

The website will also be bilingual: English and Spanish.

I don't want something high style or anything fancy; I'm just looking for a design that reflects what I do in a very natural, honest and straightforward way.

The logo also needs to reflect what I explained above. The logo name will be my name Teodo Marvel. The reason behind it is because the services that I offered are a very personalized and authentic job, and every project is different. I want the logo to reflect precisely that.

I'm attaching a lot of different photos from real projects that I did that can be used to create the design. I don't want to use everything because I want to keep it simple, at most three projects at a time showing a few pictures before and after the project is finished. The website will be created using Wordpress so that it will be dynamic, and projects will be updated regularly.

These are some websites that I like, and they can be used as inspiration and also attached I'm attaching a folder called inspiration:
- https://www.joramwexley.example (I like this one)
- https://www.tavroq.example/en
- https://www.portfolia.example/gallery/40296815/Tile-Renovation-Company
- https://www.casaplano.example/libros_de_ideas/5820463/la-belleza-del-ladrillo-en-la-decoracion-de-interiores (This one is more to highlight how by using bricks in decoration you can create exceptional spaces).

Target Market(s)

Architects, Interior Designers, Small Businesses and Home owners.

Industry/Entity Type

Interior Decoration

Logo Text

Teodo Marvel

Number of Pages Required

3 page

Font styles to use
Sans Serif

Requirements
Must have
• Landing page (with bio), project template page and contact page.
Nice to have
• Highlighting the option to showcase my products by booking a meeting.
Should not have
• Nothing unprofessional.

```html
<!DOCTYPE html>
<html lang="en">
<head>
<meta charset="utf-8">
<title>Teodo Marvel – Rustic Interiors</title>
<link href="https://fonts.googleapis.com/css2?family=Caveat+Brush&family=Montserrat:wght@500;600;700&family=Sen:wght@400;700&display=swap" rel="stylesheet">
<style>
:root{
  --board:#5b5b5b;
  --blue:#0a8fd8;
  --white:#ffffff;
  --ink:#1d1d1d;
  --muted:#8a8a8a;
  --soft:#f7f7f7;
  --footer:#474747;
  --night:#000000;
  --night-2:#111111;
  --brush:"Caveat Brush",cursive;
  --sans:"Sen",sans-serif;
  --logo:"Montserrat",sans-serif;
}
*{box-sizing:border-box;margin:0;padding:0}
html,body{width:737px;height:1200px;overflow:hidden;background:var(--board)}
.board{position:relative;width:737px;height:1200px}
.page{position:absolute;top:37px;width:622px;height:2312px;transform:scale(.4874);transform-origin:0 0;overflow:hidden;font-family:var(--sans);box-shadow:0 10px 30px rgba(0,0,0,.35)}
.page--light{left:48px;background:var(--white)}
.page--dark{left:386px;background:var(--night)}
.abs{position:absolute}
.hero{left:0;top:0;width:622px;height:348px;background:linear-gradient(160deg,#6a6a6a 0%,#3b3b3b 40%,#1c1c22 70%,#1b2c55 100%)}
.nav-logo{left:75px;top:14px;display:flex;align-items:center;gap:8px;color:var(--white);font-family:var(--logo);font-weight:600;font-size:17px;line-height:19px}
.nav-logo .mark{width:34px;height:34px;background:var(--blue)}
.nav-links{left:249px;top:27px;display:flex;gap:12px;font-size:7.5px;color:var(--white);letter-spacing:.3px}
.nav-links .active{border-bottom:2px solid var(--blue);padding-bottom:5px}
.lang{left:410px;top:24px;width:46px;height:16px;border:1px solid #aaa;color:var(--white);font-size:5.5px;display:flex;align-items:center;gap:3px;padding-left:5px}
.lang i{width:12px;height:8px;background:#3a4d8c;display:block}
.btn{background:var(--blue);color:var(--white);font-weight:700;font-size:7px;display:flex;align-items:center;justify-content:center;letter-spacing:.3px}
.nav-cta{left:463px;top:23px;width:83px;height:18px}
.hero-title{left:0;width:622px;top:100px;text-align:center;font-family:var(--brush);font-size:60px;color:var(--white)}
.hero-sub{left:0;width:622px;top:186px;text-align:center;font-size:9px;font-weight:700;color:var(--white)}
.play{left:292px;top:224px;width:38px;height:38px}
.peak{left:0;top:320px;width:622px;height:40px}
.photo{background:linear-gradient(135deg,#b9b1a8,#7e5a4c 60%,#4b3a34)}
.photo--a{left:61px;top:332px;width:244px;height:246px;clip-path:polygon(0 14px,100% 0,100% 100%,0 100%)}
.photo--b{left:317px;top:332px;width:244px;height:246px;background:linear-gradient(135deg,#d8d4cf,#a89d92 55%,#6d5f55);clip-path:polygon(0 0,100% 14px,100% 100%,0 100%)}
.h-brush{left:0;width:622px;text-align:center;font-family:var(--brush);font-size:28px;color:var(--ink)}
.bio-text{left:71px;width:480px;top:656px;text-align:center;font-size:7.6px;line-height:14.6px;color:var(--muted)}
.bio-btn{left:271px;top:731px;width:80px;height:22px}
.projects-bg{left:0;top:786px;width:622px;height:1066px}
.project-img{width:256px;height:254px}
.card{width:255px;height:196px;background:var(--white);box-shadow:0 2px 10px rgba(0,0,0,.08);padding:27px 30px}
.card .label{font-size:8px;color:var(--blue);font-weight:700;letter-spacing:.3px}
.card h3{font-size:10.5px;line-height:14px;font-weight:700;color:var(--ink);margin-top:10px;width:170px}
.card p{font-size:7.3px;line-height:13.6px;color:var(--muted);margin-top:13px}
.card .btn{width:69px;height:22px;margin-top:19px}
.pager{top:1797px;width:22px;height:22px;border:1px solid #999;background:var(--white);display:flex;align-items:center;justify-content:center}
.footer{left:0;top:1852px;width:622px;height:460px;background:var(--footer);color:var(--white)}
.f-title{left:73px;top:52px;font-family:var(--brush);font-size:28px}
.f-desc{left:74px;top:94px;width:210px;font-size:7.3px;line-height:13.5px}
.field{left:74px;width:210px;height:20px;border-bottom:1px solid #8c8c8c;font-size:7px;color:#ddd}
.submit{left:74px;top:381px;width:111px;height:26px}
.demo-img{left:332px;top:38px;width:215px;height:178px;background:linear-gradient(160deg,#9a9a9a 0%,#7c7c7c 55%,#5e5e5e 100%);clip-path:polygon(0 14px,100% 0,100% 100%,0 100%)}
.addr-h{left:332px;top:238px;font-size:10px;font-weight:700;letter-spacing:.3px}
.addr{left:332px;top:262px;font-size:7.3px;line-height:11px;display:flex;gap:5px}
.call{left:332px;top:311px;display:flex;align-items:center;gap:9px}
.call b{display:block;font-size:10px;letter-spacing:.3px}
.call strong{display:block;font-size:12.5px;letter-spacing:.3px}
.social{left:332px;top:355px;display:flex;gap:5px}
.social span{width:18px;height:18px;border-radius:50%;background:#1d4f9e}
.social span+span{background:var(--blue)}
.copy{left:332px;top:398px;font-size:6.6px}
.page--dark .h-brush{color:var(--white)}
.page--dark .bio-text{color:#d0d0d0}
.page--dark .pager--prev{background:var(--blue);border-color:var(--blue)}
</style>
</head>
<body>
<div class="board">

<main class="page page--light">
  <div class="abs hero" role="img" aria-label="Photo of a rustic stone staircase with warm lights"></div>
  <div class="abs nav-logo"><span class="mark"></span><span>TEODO<br>MARVEL</span></div>
  <nav class="abs nav-links"><span class="active">HOME</span><span>BIO</span><span>PROJECTS</span><span>CONTACT</span></nav>
  <div class="abs lang"><i></i>ENG ▾</div>
  <div class="abs btn nav-cta">REQUEST A DEMO</div>
  <h1 class="abs hero-title">Teodo Marvel</h1>
  <p class="abs hero-sub">Sed ut perspiciatis unde omnis iste natus error sit voluptatem</p>
  <svg class="abs play" viewBox="0 0 38 38"><circle cx="19" cy="19" r="17" fill="none" stroke="#fff" stroke-width="3"/><path d="M15 12 L26 19 L15 26Z" fill="#fff"/></svg>
  <svg class="abs peak" viewBox="0 0 622 40" preserveAspectRatio="none"><path d="M0 28 L311 5 L622 28 L622 40 L0 40Z" fill="#fff"/></svg>
  <div class="abs photo photo--a" role="img" aria-label="Craftsman fitting rustic bricks to a wall"></div>
  <div class="abs photo photo--b" role="img" aria-label="Portrait of the craftsman in a work coat"></div>

  <h2 class="abs h-brush" style="top:606px">ABOUT BIO</h2>
  <p class="abs bio-text">Lorem ipsum dolor sit amet, consectetur adipiscing elit, sed do eiusmod tempor incididunt ut labore et dolore magna aliquais ipsum suspendisse ultrices gravida. Risus commodo viverra maecenas accumsan lacus vel facilisis. Lorem ipsuuis ipsum suspendisse ultrices gravida. Risus commodo viverra maeauis ipsum suspendisse ultrices gravida. Risus commodo viverra maecenas accumsan lacus vel facilisis. Lorem ipsuuisauis ipsum suspendisse ultrices gravida.</p>
  <div class="abs btn bio-btn">READ MORE</div>

  <svg class="abs projects-bg" viewBox="0 0 622 1066" preserveAspectRatio="none"><path d="M0 29 L311 0 L622 29 L622 1066 L0 1066Z" fill="#f7f7f7"/></svg>
  <h2 class="abs h-brush" style="top:828px">OUR PROJECTS</h2>

  <div class="abs project-img" style="left:275px;top:899px;background:linear-gradient(160deg,#6b5a3e,#c9bd8a 40%,#4c3a2a 75%,#2a2038)" role="img" aria-label="Lit stone wall above a wooden bar"></div>
  <article class="abs card" style="left:90px;top:928px"><div class="label">PROJECT 1</div><h3>Sed ut perspiciatis unde omnis iste natus eruptatem</h3><p>Lorem ipsum dolor sit amet, consectetur adipiscing elit, sed do eiusmod tempor incididunt ut labore et dolore magna aliquis ipsum</p><div class="btn">READ MORE</div></article>

  <div class="abs project-img" style="left:90px;top:1204px;background:linear-gradient(135deg,#c49a78,#8d6043 50%,#5b3c2b)" role="img" aria-label="Brick wall around a wooden window"></div>
  <article class="abs card" style="left:276px;top:1232px"><div class="label">PROJECT 2</div><h3>Sed ut perspiciatis unde omnis iste natus eruptatem</h3><p>Lorem ipsum dolor sit amet, consectetur adipiscing elit, sed do eiusmod tempor incididunt ut labore et dolore magna aliquis ipsum</p><div class="btn">READ MORE</div></article>

  <div class="abs project-img" style="left:275px;top:1508px;background:linear-gradient(160deg,#5f8aa0,#a0553a 30%,#7a3a26 65%,#3a2a22)" role="img" aria-label="Red brick wall with a hexagonal wooden sign"></div>
  <article class="abs card" style="left:90px;top:1537px"><div class="label">PROJECT 3</div><h3>Sed ut perspiciatis unde omnis iste natus eruptatem</h3><p>Lorem ipsum dolor sit amet, consectetur adipiscing elit, sed do eiusmod tempor incididunt ut labore et dolore magna aliquis ipsum</p><div class="btn">READ MORE</div></article>

  <div class="abs pager pager--prev" style="left:285px"><svg width="8" height="10" viewBox="0 0 8 10"><path d="M6 1 L2 5 L6 9" fill="none" stroke="#222" stroke-width="1.3"/></svg></div>
  <div class="abs pager" style="left:313px"><svg width="8" height="10" viewBox="0 0 8 10"><path d="M2 1 L6 5 L2 9" fill="none" stroke="#222" stroke-width="1.3"/></svg></div>

  <footer class="abs footer">
    <h2 class="abs f-title">REQUEST A DEMO</h2>
    <p class="abs f-desc">Lorem ipsum dolor sit amet, consectetur adipiscing elit, sed do eiusmod tempor incididunt</p>
    <div class="abs field" style="top:150px">Enter Name</div>
    <div class="abs field" style="top:193px">Enter Email</div>
    <div class="abs field" style="top:236px">Phone</div>
    <div class="abs field" style="top:280px;display:flex;justify-content:space-between">Services<span>▾</span></div>
    <div class="abs field" style="top:320px;height:44px">Message</div>
    <div class="abs btn submit">SUBMIT MESSAGE</div>
    <div class="abs demo-img" role="img" aria-label="Photo of a product demo with a lighting remote among stones"></div>
    <div class="abs addr-h">ADDRESS</div>
    <div class="abs addr"><svg width="7" height="10" viewBox="0 0 7 10"><path d="M3.5 0 A3.5 3.5 0 0 1 7 3.5 C7 6 3.5 10 3.5 10 C3.5 10 0 6 0 3.5 A3.5 3.5 0 0 1 3.5 0Z" fill="#fff"/><circle cx="3.5" cy="3.5" r="1.3" fill="#474747"/></svg><span>123,Sed ut perspiciatis unde omnis isatus<br>error sluptatem accusantium</span></div>
    <div class="abs call"><svg width="24" height="24" viewBox="0 0 24 24"><circle cx="12" cy="12" r="11" fill="none" stroke="#fff" stroke-width="1.6"/><path d="M8 7 L10 7 L11 10 L9.6 11 C10.4 12.6 11.4 13.6 13 14.4 L14 13 L17 14 L17 16 C12 17 7 12 8 7Z" fill="#fff"/></svg><div><b>CALL US</b><strong>1 888 888 8888</strong></div></div>
    <div class="abs social"><span aria-label="Friendnook"></span><span aria-label="Chirpline"></span></div>
    <p class="abs copy">© 2020 Copyright Teodo Marvel . All Rights Reserved &nbsp;| &nbsp;Terms and Conditions</p>
  </footer>
</main>

<main class="page page--dark">
  <div class="abs hero" role="img" aria-label="Photo of a rustic stone staircase with warm lights"></div>
  <div class="abs nav-logo"><span class="mark"></span><span>TEODO<br>MARVEL</span></div>
  <nav class="abs nav-links"><span class="active">HOME</span><span>BIO</span><span>PROJECTS</span><span>CONTACT</span></nav>
  <div class="abs lang"><i></i>ENG ▾</div>
  <div class="abs btn nav-cta">REQUEST A DEMO</div>
  <h1 class="abs hero-title">Teodo Marvel</h1>
  <p class="abs hero-sub">Sed ut perspiciatis unde omnis iste natus error sit voluptatem</p>
  <svg class="abs play" viewBox="0 0 38 38"><circle cx="19" cy="19" r="17" fill="none" stroke="#fff" stroke-width="3"/><path d="M15 12 L26 19 L15 26Z" fill="#fff"/></svg>
  <svg class="abs peak" viewBox="0 0 622 40" preserveAspectRatio="none"><path d="M0 28 L311 5 L622 28 L622 40 L0 40Z" fill="#000"/></svg>
  <div class="abs photo photo--a" role="img" aria-label="Craftsman fitting rustic bricks to a wall"></div>
  <div class="abs photo photo--b" role="img" aria-label="Portrait of the craftsman in a work coat"></div>

  <h2 class="abs h-brush" style="top:606px">ABOUT BIO</h2>
  <p class="abs bio-text">Lorem ipsum dolor sit amet, consectetur adipiscing elit, sed do eiusmod tempor incididunt ut labore et dolore magna aliquais ipsum suspendisse ultrices gravida. Risus commodo viverra maecenas accumsan lacus vel facilisis. Lorem ipsuuis ipsum suspendisse ultrices gravida. Risus commodo viverra maeauis ipsum suspendisse ultrices gravida. Risus commodo viverra maecenas accumsan lacus vel facilisis. Lorem ipsuuisauis ipsum suspendisse ultrices gravida.</p>
  <div class="abs btn bio-btn">READ MORE</div>

  <svg class="abs projects-bg" viewBox="0 0 622 1066" preserveAspectRatio="none"><path d="M0 29 L311 0 L622 29 L622 1066 L0 1066Z" fill="#111"/><path d="M60 24 L311 0 L562 24" fill="none" stroke="#0a8fd8" stroke-width="2"/></svg>
  <h2 class="abs h-brush" style="top:828px">OUR PROJECTS</h2>

  <div class="abs project-img" style="left:275px;top:899px;background:linear-gradient(160deg,#6b5a3e,#c9bd8a 40%,#4c3a2a 75%,#2a2038)" role="img" aria-label="Lit stone wall above a wooden bar"></div>
  <article class="abs card" style="left:90px;top:928px"><div class="label">PROJECT 1</div><h3>Sed ut perspiciatis unde omnis iste natus eruptatem</h3><p>Lorem ipsum dolor sit amet, consectetur adipiscing elit, sed do eiusmod tempor incididunt ut labore et dolore magna aliquis ipsum</p><div class="btn">READ MORE</div></article>

  <div class="abs project-img" style="left:90px;top:1204px;background:linear-gradient(135deg,#c49a78,#8d6043 50%,#5b3c2b)" role="img" aria-label="Brick wall around a wooden window"></div>
  <article class="abs card" style="left:276px;top:1232px"><div class="label">PROJECT 2</div><h3>Sed ut perspiciatis unde omnis iste natus eruptatem</h3><p>Lorem ipsum dolor sit amet, consectetur adipiscing elit, sed do eiusmod tempor incididunt ut labore et dolore magna aliquis ipsum</p><div class="btn">READ MORE</div></article>

  <div class="abs project-img" style="left:275px;top:1508px;background:linear-gradient(160deg,#5f8aa0,#a0553a 30%,#7a3a26 65%,#3a2a22)" role="img" aria-label="Red brick wall with a hexagonal wooden sign"></div>
  <article class="abs card" style="left:90px;top:1537px"><div class="label">PROJECT 3</div><h3>Sed ut perspiciatis unde omnis iste natus eruptatem</h3><p>Lorem ipsum dolor sit amet, consectetur adipiscing elit, sed do eiusmod tempor incididunt ut labore et dolore magna aliquis ipsum</p><div class="btn">READ MORE</div></article>

  <div class="abs pager pager--prev" style="left:285px"><svg width="8" height="10" viewBox="0 0 8 10"><path d="M6 1 L2 5 L6 9" fill="none" stroke="#fff" stroke-width="1.3"/></svg></div>
  <div class="abs pager" style="left:313px"><svg width="8" height="10" viewBox="0 0 8 10"><path d="M2 1 L6 5 L2 9" fill="none" stroke="#222" stroke-width="1.3"/></svg></div>

  <footer class="abs footer">
    <h2 class="abs f-title">REQUEST A DEMO</h2>
    <p class="abs f-desc">Lorem ipsum dolor sit amet, consectetur adipiscing elit, sed do eiusmod tempor incididunt</p>
    <div class="abs field" style="top:150px">Enter Name</div>
    <div class="abs field" style="top:193px">Enter Email</div>
    <div class="abs field" style="top:236px">Phone</div>
    <div class="abs field" style="top:280px;display:flex;justify-content:space-between">Services<span>▾</span></div>
    <div class="abs field" style="top:320px;height:44px">Message</div>
    <div class="abs btn submit">SUBMIT MESSAGE</div>
    <div class="abs demo-img" role="img" aria-label="Photo of a product demo with a lighting remote among stones"></div>
    <div class="abs addr-h">ADDRESS</div>
    <div class="abs addr"><svg width="7" height="10" viewBox="0 0 7 10"><path d="M3.5 0 A3.5 3.5 0 0 1 7 3.5 C7 6 3.5 10 3.5 10 C3.5 10 0 6 0 3.5 A3.5 3.5 0 0 1 3.5 0Z" fill="#fff"/><circle cx="3.5" cy="3.5" r="1.3" fill="#474747"/></svg><span>123,Sed ut perspiciatis unde omnis isatus<br>error sluptatem accusantium</span></div>
    <div class="abs call"><svg width="24" height="24" viewBox="0 0 24 24"><circle cx="12" cy="12" r="11" fill="none" stroke="#fff" stroke-width="1.6"/><path d="M8 7 L10 7 L11 10 L9.6 11 C10.4 12.6 11.4 13.6 13 14.4 L14 13 L17 14 L17 16 C12 17 7 12 8 7Z" fill="#fff"/></svg><div><b>CALL US</b><strong>1 888 888 8888</strong></div></div>
    <div class="abs social"><span aria-label="Friendnook"></span><span aria-label="Chirpline"></span></div>
    <p class="abs copy" style="top:402px">© 2020 Copyright Teodo Marvel . All Rights Reserved &nbsp;| &nbsp;Terms and Conditions</p>
  </footer>
</main>

</div>
</body>
</html>
```